Company Values Graphic

We are looking for a design of our company values that can be used in a variety of places including our website, mousepads, office posters, business cards, etc.

Notes:
- We'd rather have icons/art than photographs on the poster.... so more like an infographic
- The core value group headings are not required, but can be included if you think grouping the values works for your design
- We have a logo for our software product but that logo is not required
- We don't need/want clever images to accompany each value, but some images are fine
- BrisKel logo attached
- BrisKel colors are attached
- BrisKel logo is Nunito Sans ExtraBold 800
- BrisKel website uses Roboto

Our Values - Who we will work with (and who we will not)
The right set of values are essential to building and maintaining a culture that we all wake up eager to be a part of each day. They are foundational to all hiring and firing decisions. They attract the right people and repel the wrong ones.

BE HELPFUL
Make every person and place better because you are there.
Deliver wow with every interaction.

BE HUMBLE
Listen with every muscle.
Passionately help others first.
Seek first to understand.

BE HONEST
Earn trust every day.
Be open and direct.
Treat everyone with fairness and respect.

BE HUMAN
Celebrate passion and action.
Create an environment where people are authentic.
Hire great people and expect a lot from them

BE COURAGEOUS
Dare mighty things.
Make and honor commitments.
All great things start with a small act of courage applied at the right moment.

```html
<!DOCTYPE html>
<html lang="en">
<head>
<meta charset="utf-8">
<title>Our Values – Who we will work with</title>
<link rel="stylesheet" href="https://fonts.googleapis.com/css2?family=Nunito+Sans:wght@800;900&family=Roboto:wght@400;500&display=swap">
<style>
  :root {
    --backdrop: #2e2e2e;
    --paper: #ffffff;
    --red: #ed1f27;
    --amber: #f79a20;
    --orange: #f26522;
    --ink: #0a0a0a;
    --rule: #ececec;
  }
  html, body {
    margin: 0;
    width: 1200px;
    height: 1200px;
    overflow: hidden;
    background: var(--backdrop);
  }
  .poster {
    position: absolute;
    left: 224px;
    top: 73px;
    width: 752px;
    height: 1054px;
    display: block;
    background: var(--paper);
  }
  .display { font-family: "Nunito Sans", sans-serif; font-weight: 900; fill: var(--ink); }
  .title { font-family: "Nunito Sans", sans-serif; font-weight: 800; fill: var(--paper); font-size: 44px; }
  .subtitle { font-family: "Nunito Sans", sans-serif; font-weight: 800; fill: var(--ink); font-size: 26px; }
  .intro { font-family: Roboto, sans-serif; font-size: 15px; fill: var(--paper); }
  .value-be { font-family: "Nunito Sans", sans-serif; font-weight: 800; font-size: 23px; fill: var(--ink); }
  .value-name { font-family: "Nunito Sans", sans-serif; font-weight: 900; font-size: 35px; fill: var(--orange); }
  .value-point { font-family: Roboto, sans-serif; font-size: 15.5px; fill: var(--ink); }
  .tick circle { fill: none; stroke: var(--orange); stroke-width: 1.1; }
  .tick path { fill: none; stroke: var(--orange); stroke-width: 1.2; stroke-linecap: round; stroke-linejoin: round; }
  .icon-slot { fill: #e9e9e9; }
  .divider { stroke: var(--rule); stroke-width: 2; }
  .dotted-edge { fill: none; stroke: var(--ink); stroke-width: 2; stroke-dasharray: 0.1 6; stroke-linecap: round; }
</style>
</head>
<body>
<svg class="poster" viewBox="0 0 752 1054" xmlns="http://www.w3.org/2000/svg">
  <defs>
    <g id="tick" class="tick">
      <circle cx="0" cy="0" r="5"/>
      <path d="M-2.4 0.2 L-0.6 2 L2.6 -1.8"/>
    </g>
  </defs>

  <!-- header band -->
  <path d="M29 0 C 80 150 190 188 300 188 L 600 188 C 680 188 720 215 752 241 L 752 0 Z" fill="var(--red)"/>

  <!-- dividers -->
  <line class="divider" x1="280" y1="347" x2="752" y2="347"/>
  <line class="divider" x1="352" y1="523" x2="752" y2="523"/>
  <line class="divider" x1="320" y1="702" x2="752" y2="702"/>
  <line class="divider" x1="190" y1="879" x2="752" y2="879"/>

  <!-- amber drop -->
  <path class="dotted-edge" d="M0 50 L 274 322 C 345 395 357 470 357 555 C 357 765 185 909 0 909"/>
  <path d="M0 62 L 266 325 C 330 390 347 470 347 555 C 347 760 180 899 0 899 Z" fill="var(--amber)"/>

  <text class="display" font-size="104" transform="translate(105 647) rotate(-90)">Our</text>
  <text class="display" font-size="122" transform="translate(224 847) rotate(-90)">Values -</text>

  <!-- header text -->
  <text class="title" x="727" y="55" text-anchor="end">Who we will work with</text>
  <text class="subtitle" x="727" y="86" text-anchor="end">(and who we will not)</text>
  <text class="intro" text-anchor="end">
    <tspan x="727" y="122">The right set of values are essential to building and maintaining a culture that we all wake</tspan>
    <tspan x="727" y="140">up eager to be a part of each day. They are foundational to all hiring and firing</tspan>
    <tspan x="727" y="158">decisions. They attract the right people and repel the wrong ones.</tspan>
  </text>

  <!-- helpful -->
  <rect class="icon-slot" x="218" y="210" width="60" height="60" rx="6" role="img" aria-label="Handshake icon"/>
  <text class="value-be" x="291" y="232">BE</text>
  <text class="value-name" x="291" y="265">HELPFUL</text>
  <use href="#tick" x="295" y="289"/>
  <text class="value-point" x="306" y="294">Make every person and place better because you are there.</text>
  <use href="#tick" x="295" y="313"/>
  <text class="value-point" x="306" y="318">Deliver wow with every interaction.</text>

  <!-- humble -->
  <rect class="icon-slot" x="332" y="370" width="56" height="62" rx="6" role="img" aria-label="Head with heart icon"/>
  <text class="value-be" x="400" y="391">BE</text>
  <text class="value-name" x="400" y="422">HUMBLE</text>
  <use href="#tick" x="404" y="447"/>
  <text class="value-point" x="420" y="452">Listen with every muscle.</text>
  <use href="#tick" x="404" y="470"/>
  <text class="value-point" x="420" y="475">Passionately help others first.</text>
  <use href="#tick" x="404" y="495"/>
  <text class="value-point" x="420" y="500">Seek first to understand.</text>

  <!-- honest -->
  <rect class="icon-slot" x="362" y="546" width="58" height="63" rx="6" role="img" aria-label="Hand holding a star icon"/>
  <text class="value-be" x="433" y="568">BE</text>
  <text class="value-name" x="433" y="601">HONEST</text>
  <use href="#tick" x="437" y="626"/>
  <text class="value-point" x="448" y="631">Earn trust every day.</text>
  <use href="#tick" x="437" y="649"/>
  <text class="value-point" x="448" y="654">Be open and direct.</text>
  <use href="#tick" x="437" y="674"/>
  <text class="value-point" x="448" y="679">Treat everyone with fairness and respect.</text>

  <!-- human -->
  <rect class="icon-slot" x="310" y="722" width="52" height="62" rx="6" role="img" aria-label="Group of people icon"/>
  <text class="value-be" x="377" y="746">BE</text>
  <text class="value-name" x="377" y="778">HUMAN</text>
  <use href="#tick" x="381" y="802"/>
  <text class="value-point" x="394" y="807">Celebrate passion and action.</text>
  <use href="#tick" x="381" y="826"/>
  <text class="value-point" x="394" y="831">Create an environment where people are authentic.</text>
  <use href="#tick" x="381" y="851"/>
  <text class="value-point" x="394" y="856">Hire great people and expect a lot from them.</text>

  <!-- courageous -->
  <rect class="icon-slot" x="108" y="892" width="48" height="57" rx="6" role="img" aria-label="Raised fist icon"/>
  <text class="value-be" x="170" y="915">BE</text>
  <text class="value-name" x="170" y="947">COURAGEOUS</text>
  <use href="#tick" x="174" y="972"/>
  <text class="value-point" x="186" y="977">Dare mighty things.</text>
  <use href="#tick" x="174" y="995"/>
  <text class="value-point" x="186" y="1000">Make and honor commitments.</text>
  <use href="#tick" x="174" y="1020"/>
  <text class="value-point" x="186" y="1025">All great things start with a small act of courage applied at the right moment.</text>
</svg>
</body>
</html>
```